Flyer for spiritual retreat (yoga, meditation, reiki, raw food)

I would like a flyer to promote my upcoming retreat and a matching Facebook banner.

The name of the retreat is "Blossomreach Within" and the tagline is "retreat into you"

The activities in the retreat include daily meditation, ecstatic dance, spiritual development workshops on intuition, energy healing etc and a reiki session is included.

I would like a flyer designed to promote this, something that is editable as I will be running this multiple times and will need to adjust the flyer to add the dates etc each time.

edit: add that here will be fully catered raw food and juices, and that the retreat price includes all accomodation, meals and workshops.

Please contact me if you need further info. Please also visit my website www.marniekovac-studio.com and www.friendhub-sample.com/tuvelanook to see my current events and promotions.

Thank you,

Marnie

Reason: Hi all, thank you all for your submissions. Apologies as I am traveling and do not have much access to internet and will review your submissions and provide feedback as soon as possible. Kind regards, Marnie.

Target Market(s)

People who like meditation, yoga, fans of ronan feldspar and mervin okoro, those interested in personal and spiritual development.

Industry/Entity Type

Health And Wellness

Requirements
Must have
• Please put the included reiki session as as added bonus. Something like "BONUS 30 minute reiki healing session" in a little star/banner/something that stands out.
• Please emphasise the "light" part of Blossomreach as I am going for a play on words between in the light and enlightenment.
• Please include placeholder text for place, location, time
• Placeholder for price
• My name (see attached file - can change colour to suit) and website (www.marniekovac-studio.com)
Nice to have
• I prefer rounded designs, curves rather than block designs.
Should not have
• Tuvela Nook logo

```html
<!DOCTYPE html>
<html lang="en">
<head>
<meta charset="utf-8">
<title>Blossomreach Within – Retreat Flyer</title>
<link rel="stylesheet" href="https://fonts.googleapis.com/css2?family=Raleway:wght@400;500;600&family=Great+Vibes&display=swap">
<style>
  :root {
    --purple-deep: #6f4596;
    --purple: #7c4f9f;
    --purple-light: #9466b8;
    --lilac-text: #7a4aa0;
    --pink: #e7a3cb;
    --pale: #f3f5ea;
    --pale-green: #dfe6d0;
    --white: #ffffff;
    --yellow: #f4ea2a;
    --backdrop: #e4e4e4;
  }
  * { margin: 0; padding: 0; box-sizing: border-box; }
  html, body { width: 902px; height: 1200px; overflow: hidden; background: var(--backdrop); }
  .stage { position: relative; width: 902px; height: 1200px; }
  .flyer {
    position: absolute; left: 26.5px; top: 0;
    width: 984px; height: 1391px;
    transform: scale(0.8627); transform-origin: 0 0;
    overflow: hidden;
    font-family: "Raleway", sans-serif;
  }
  .flyer-bg { position: absolute; inset: 0; width: 100%; height: 100%; }
  .abs { position: absolute; }

  .title {
    left: 0; width: 984px; top: 62px; text-align: center;
    font-size: 66px; font-weight: 400; letter-spacing: 4px; color: var(--white);
    text-shadow: 0 2px 6px rgba(60,20,90,.45);
  }
  .title .highlight { color: var(--yellow); }

  .tagline {
    left: 495px; top: 236px; font-family: "Great Vibes", cursive;
    font-size: 82px; color: var(--lilac-text); white-space: nowrap;
  }

  .features { left: 543px; top: 378px; list-style: none; }
  .features li {
    height: 57.5px; display: flex; align-items: center;
    font-size: 22px; font-weight: 500; letter-spacing: .5px; color: var(--lilac-text);
  }
  .features svg { width: 26px; height: 22px; margin-right: 21px; }

  .dates {
    left: 78px; top: 832px; font-size: 96px; font-weight: 400; line-height: 96px;
    background: linear-gradient(120deg, #c084c2 0%, #8c63b6 45%, #6f5fb5 100%);
    -webkit-background-clip: text; background-clip: text; color: transparent;
  }
  .divider { left: 572px; top: 845px; width: 2px; height: 125px; background: var(--lilac-text); }
  .location { left: 603px; top: 846px; width: 300px; font-size: 20px; line-height: 40px; color: var(--lilac-text); letter-spacing: .5px; }
  .location strong { font-weight: 600; }

  .price { left: 77px; top: 1104px; color: var(--white); }
  .price .from { font-size: 22px; }
  .price .amount { display: flex; align-items: flex-end; }
  .price .figure { font-size: 62px; line-height: 62px; }
  .price .per { font-size: 22px; line-height: 20px; margin-left: 8px; margin-bottom: 8px; }
  .price p { font-size: 20px; line-height: 26px; letter-spacing: .5px; margin-top: 14px; }

  .host { color: var(--white); white-space: nowrap; text-align: right; }
  .host-label { right: 96px; top: 1070px; font-size: 20px; }
  .host-name { right: 50px; top: 1098px; font-family: "Great Vibes", cursive; font-size: 84px; line-height: 110px; }
  .website { right: 56px; top: 1250px; font-size: 25px; letter-spacing: 1px; }
  .email { right: 56px; top: 1305px; font-size: 25px; letter-spacing: 1px; display: flex; align-items: center; gap: 20px; }
</style>
</head>
<body>
<div class="stage">
  <div class="flyer">
    <svg class="flyer-bg" viewBox="0 0 984 1391" preserveAspectRatio="none">
      <defs>
        <linearGradient id="purpleBand" x1="0" y1="0" x2="1" y2="1">
          <stop offset="0" stop-color="#8d5cb0"/>
          <stop offset="1" stop-color="#7048a0"/>
        </linearGradient>
        <radialGradient id="paleField" cx="0.55" cy="0.45" r="0.7">
          <stop offset="0" stop-color="#f7f8f0"/>
          <stop offset="1" stop-color="#dfe6d0"/>
        </radialGradient>
        <linearGradient id="portraitTone" x1="0" y1="0" x2="1" y2="1">
          <stop offset="0" stop-color="#b9d49a"/>
          <stop offset="0.5" stop-color="#8a7a8e"/>
          <stop offset="1" stop-color="#a993c4"/>
        </linearGradient>
      </defs>
      <rect width="984" height="1391" fill="url(#purpleBand)"/>
      <path d="M0,290 C200,230 560,175 984,180 L984,850 C800,980 560,1110 360,1135 L0,1135 Z" fill="url(#paleField)"/>
      <path d="M360,238 C560,185 780,178 984,182 L984,194 C780,192 570,200 372,246 Z" fill="var(--pink)"/>
      <path d="M984,842 C820,960 600,1100 362,1138 L380,1148 C620,1110 840,990 984,872 Z" fill="var(--pink)"/>
      <path d="M984,872 C840,990 620,1110 380,1148 L984,1148 Z" fill="url(#purpleBand)"/>
      <ellipse cx="150" cy="1420" rx="312" ry="382" fill="var(--white)"/>
      <ellipse cx="150" cy="1420" rx="306" ry="376" fill="var(--purple)"/>
      <circle cx="247" cy="488" r="255" fill="var(--white)"/>
      <circle cx="247" cy="488" r="250" fill="url(#portraitTone)" role="img" aria-label="Portrait photo of the retreat host in a garden, hands together"/>
    </svg>

    <h1 class="abs title">BLOSSOM<span class="highlight">REACH</span> WITHIN</h1>
    <div class="abs tagline">Retreat into You</div>

    <ul class="abs features">
      <li><svg viewBox="0 0 26 22"><path d="M1 7 L7 1 H19 L25 7 L13 21 Z" fill="#8b5cc0"/><path d="M1 7 H25 M7 1 L13 21 L19 1" stroke="#c8acec" stroke-width="1" fill="none"/></svg>DAILY MEDITATION</li>
      <li><svg viewBox="0 0 26 22"><path d="M1 7 L7 1 H19 L25 7 L13 21 Z" fill="#8b5cc0"/><path d="M1 7 H25 M7 1 L13 21 L19 1" stroke="#c8acec" stroke-width="1" fill="none"/></svg>ECSTATIC DANCE</li>
      <li><svg viewBox="0 0 26 22"><path d="M1 7 L7 1 H19 L25 7 L13 21 Z" fill="#8b5cc0"/><path d="M1 7 H25 M7 1 L13 21 L19 1" stroke="#c8acec" stroke-width="1" fill="none"/></svg>DAILY WORKSHOPS</li>
      <li><svg viewBox="0 0 26 22"><path d="M1 7 L7 1 H19 L25 7 L13 21 Z" fill="#8b5cc0"/><path d="M1 7 H25 M7 1 L13 21 L19 1" stroke="#c8acec" stroke-width="1" fill="none"/></svg>ENERGY HEALING</li>
      <li><svg viewBox="0 0 26 22"><path d="M1 7 L7 1 H19 L25 7 L13 21 Z" fill="#8b5cc0"/><path d="M1 7 H25 M7 1 L13 21 L19 1" stroke="#c8acec" stroke-width="1" fill="none"/></svg>SPIRITUAL DEVELOPMENT</li>
      <li><svg viewBox="0 0 26 22"><path d="M1 7 L7 1 H19 L25 7 L13 21 Z" fill="#8b5cc0"/><path d="M1 7 H25 M7 1 L13 21 L19 1" stroke="#c8acec" stroke-width="1" fill="none"/></svg>RAW FOOD &amp; JUICES</li>
      <li><svg viewBox="0 0 26 22"><path d="M1 7 L7 1 H19 L25 7 L13 21 Z" fill="#8b5cc0"/><path d="M1 7 H25 M7 1 L13 21 L19 1" stroke="#c8acec" stroke-width="1" fill="none"/></svg>ACCOMODATION INCLUDED</li>
    </ul>

    <div class="abs dates">DEC 26-29<br>2017</div>
    <div class="abs divider"></div>
    <div class="abs location"><strong>Location:</strong> Tallowmere, Ridgeway Hills (address given upon registration)</div>

    <div class="abs price">
      <div class="from">From</div>
      <div class="amount"><span class="figure">$1500</span><span class="per">per<br>person</span></div>
      <p>INCLUDES: all accomodation,<br>meals &amp; workshops</p>
      <p>BONUS: 30 min Energy<br>Healing Session</p>
    </div>

    <div class="abs host host-label">Hosted By:</div>
    <div class="abs host host-name">Marnie Kovac</div>
    <div class="abs host website">www.marniekovac-studio.com</div>
    <div class="abs host email">
      <svg width="32" height="22" viewBox="0 0 32 22"><rect x="1" y="1" width="30" height="20" fill="#fff"/><path d="M1 1 L16 12 L31 1" fill="none" stroke="#7c4f9f" stroke-width="2.5"/></svg>
      <span>marnie.k33@mailbox.test</span>
    </div>
  </div>
</div>
</body>
</html>
```